Quarrow financial services, is a financial company that provides consultancy, brokerage services, and funding.

we will be providing the clients with insights, knowledge and data with regards to the financial markets.

with the brokerage services we will try to find the suitable counterparts that provide them with the best investments that suits their needs and expected return.

Target Market(s)

financial institutions, Corporates, high-net worth individuals

Industry/Entity Type

Financial Service

Contact Information for Business Card

Font styles to use
Other font styles liked:
• applemyungjo

Colors
00a990
848484

Requirements
Must have
• the logo at the back
Nice to have
• Finesse
Should not have
• boldness

```html
<!DOCTYPE html>
<html lang="en">
<head>
<meta charset="utf-8">
<title>Quarrow Financial Services – Business Card</title>
<link rel="stylesheet" href="https://fonts.googleapis.com/css2?family=Open+Sans:ital,wght@0,300;0,400;1,400&display=swap">
<style>
  :root {
    --backdrop: #4a4a4a;
    --slate: #434d52;
    --leaf: #7a9b4a;
    --leaf-pale: #c9d4b8;
    --ink: #4a4a4a;
    --paper: #ffffff;
  }
  * { box-sizing: border-box; margin: 0; padding: 0; }
  html, body {
    width: 1105px; height: 1200px; overflow: hidden;
    background: var(--backdrop);
    font-family: "Open Sans", sans-serif;
  }
  .card {
    position: absolute; left: 196px; width: 720px;
  }
  .card--front { top: 170px; height: 387px; background: var(--paper); overflow: hidden; }
  .card--back { top: 602px; height: 410px; background: var(--leaf); }

  .front-swoosh { position: absolute; inset: 0; width: 100%; height: 100%; }

  .holder { position: absolute; right: 29px; top: 10px; text-align: right; }
  .holder__name { color: var(--leaf); font-size: 26px; font-weight: 400; letter-spacing: 0.5px; }
  .holder__role { color: var(--paper); font-size: 19px; font-weight: 400; margin-top: -2px; }

  .brand-square {
    position: absolute; width: 52px; height: 52px; background: var(--leaf-pale);
  }
  .card--front .brand-square { left: 112px; top: 84px; }
  .brand {
    position: absolute; left: 39px; top: 182px; width: 200px; text-align: center;
    color: var(--slate); font-weight: 300;
  }
  .brand__name { font-size: 38px; letter-spacing: 2px; line-height: 1.1; }
  .brand__line { font-size: 12px; letter-spacing: 2px; }

  .contacts { position: absolute; left: 37px; top: 280px; list-style: none; }
  .contacts li {
    display: flex; align-items: center; gap: 10px;
    height: 27.5px; color: var(--ink); font-size: 19px;
  }
  .contacts svg { width: 17px; height: 17px; fill: var(--leaf); flex: none; }

  .address {
    position: absolute; right: 29px; top: 307px; text-align: right;
    color: var(--ink); font-size: 19px; line-height: 27.5px; font-style: normal;
  }

  .back-brand {
    position: absolute; left: 0; right: 0; top: 150px;
    display: flex; align-items: center; justify-content: center; gap: 18px;
  }
  .card--back .brand-square { position: static; width: 60px; height: 60px; }
  .back-brand__name { color: var(--paper); font-size: 44px; font-weight: 300; letter-spacing: 3px; }
  .back-url {
    position: absolute; left: 0; right: 0; top: 350px; text-align: center;
    color: var(--paper); font-size: 20px; font-style: italic; letter-spacing: 2.5px;
  }
</style>
</head>
<body>
  <section class="card card--front" aria-label="Business card front">
    <svg class="front-swoosh" viewBox="0 0 521 280" preserveAspectRatio="none" aria-hidden="true">
      <path fill="var(--slate)" d="M0 0H521V138C420 50 200 -5 0 32Z"/>
      <path fill="var(--leaf)" d="M0 37C200 6 420 58 521 148V178C430 92 230 24 0 42Z"/>
    </svg>

    <div class="holder">
      <p class="holder__name">ELIAS MARLOWE</p>
      <p class="holder__role">CEO/Founder</p>
    </div>

    <span class="brand-square" aria-hidden="true"></span>
    <div class="brand">
      <p class="brand__name">QUARROW</p>
      <p class="brand__line">FINANCIAL SERVICES</p>
    </div>

    <ul class="contacts">
      <li>
        <svg viewBox="0 0 24 24" aria-hidden="true"><path d="M6.6 10.8a15 15 0 0 0 6.6 6.6l2.2-2.2a1 1 0 0 1 1-.25 11.4 11.4 0 0 0 3.6.57 1 1 0 0 1 1 1V20a1 1 0 0 1-1 1A17 17 0 0 1 3 4a1 1 0 0 1 1-1h3.5a1 1 0 0 1 1 1c0 1.25.2 2.45.57 3.57a1 1 0 0 1-.25 1z"/></svg>
        555 014 2290
      </li>
      <li>
        <svg viewBox="0 0 24 24" aria-hidden="true"><path d="M2 5h20v14H2zm2 2v.5l8 5 8-5V7l-8 5z"/></svg>
        hello@quarrowmail.com
      </li>
      <li>
        <svg viewBox="0 0 24 24" aria-hidden="true"><circle cx="12" cy="12" r="10"/><path fill="#fff" d="M8 6c2 1 1 3 3 3s1 3-1 3-2 3-1 5c-2-1-4-3-4-6 0-2 1-4 3-5zm7 9c1-2 3-2 4-1-1 3-3 4-5 5 0-2 0-3 1-4z"/></svg>
        www.quarrowmail.com
      </li>
    </ul>

    <address class="address">
      1420 Larkspur Court<br>
      Juneau, Alaska 34512
    </address>
  </section>

  <section class="card card--back" aria-label="Business card back">
    <div class="back-brand">
      <span class="brand-square" aria-hidden="true"></span>
      <p class="back-brand__name">QUARROW</p>
    </div>
    <p class="back-url">www.quarrowfinancial.com</p>
  </section>
</body>
</html>
```